We Need a Letterhead + Fax Cover Sheet for Heron Staffing

LETTERHEAD:
- Simple letterhead. Please provide an editable .doc file apart from usual Source Files. Logo Files attached for your use.
- Please place our logo on the upper right corner of the page. You may add some sort of graphic, or light colored background (depends on what looks good).
- Footer should include:
Heron Staffing, LLC
412 Kestrel Ave. Suite 118
Mobile, AL 36619

FAX COVER SHEET:
- Have the logo placed here, should be large, maybe an eight of the page.
- Put:
From:
To:
Phone Number:
Fax Number:

*Still needs some details, will update you because working on the website, etc.

Heron Coastal Workforce Services

```html
<!DOCTYPE html>
<html lang="en">
<head>
<meta charset="utf-8">
<title>Heron Staffing – Letterhead + Fax Cover Sheet</title>
<link rel="stylesheet" href="https://fonts.googleapis.com/css2?family=Montserrat:wght@500&family=Work+Sans:wght@400&family=Lato:wght@400&family=Roboto:wght@400&display=swap">
<style>
  :root {
    --board: #e0dfe0;
    --paper: #ffffff;
    --brand-blue: #0b73b5;
    --brand-green: #8aab3a;
    --ink: #3a3a3a;
    --ink-soft: #555555;
  }
  * { box-sizing: border-box; margin: 0; padding: 0; }
  html, body { width: 1200px; height: 978px; overflow: hidden; }
  body { background: var(--board); position: relative; font-family: "Work Sans", sans-serif; color: var(--ink); }

  .board-title {
    position: absolute; top: 92px; left: 0; width: 1200px; text-align: center;
    font-family: "Montserrat", sans-serif; font-weight: 500; font-size: 42px;
    letter-spacing: 1px; color: var(--brand-blue);
  }

  .page {
    position: absolute; top: 212px; width: 496px; height: 701px;
    background: var(--paper); box-shadow: 3px 3px 8px rgba(0,0,0,0.18);
  }
  .page--letter { left: 73px; }
  .page--fax { left: 632px; }

  .brand-mark {
    position: absolute; left: 0; width: 100%;
    display: flex; flex-direction: column; align-items: center; justify-content: center;
    font-family: "Work Sans", sans-serif; font-weight: 400; color: var(--brand-blue);
    text-align: center; line-height: 1.25;
  }
  .brand-mark__dot { border-radius: 50%; background: var(--brand-green); margin-bottom: 8px; }
  .page--letter .brand-mark { top: 26px; height: 128px; font-size: 15px; }
  .page--letter .brand-mark__dot { width: 34px; height: 34px; }
  .page--fax .brand-mark { top: 26px; height: 154px; font-size: 19px; }
  .page--fax .brand-mark__dot { width: 44px; height: 44px; }

  .letter-body { position: absolute; left: 36px; top: 234px; width: 430px; }
  .greeting { font-family: "Lato", sans-serif; font-size: 12px; margin-bottom: 24px; }
  .letter-body p.copy { font-size: 9.6px; line-height: 12.9px; color: var(--ink-soft); margin-bottom: 16px; }
  .sign-off { font-family: "Lato", sans-serif; font-size: 12px; margin-top: 16px; }
  .signer-name { font-family: "Lato", sans-serif; font-size: 11px; margin-top: 7px; }
  .signer-role { font-family: "Lato", sans-serif; font-size: 8px; }
  .signature {
    width: 88px; height: 14px; margin-top: 13px;
    background: linear-gradient(90deg, #6a6a6a 0%, #9a9a9a 100%); opacity: 0.35; border-radius: 3px;
  }

  .fax-heading { position: absolute; left: 32px; top: 238px; font-family: "Roboto", sans-serif; font-size: 37px; color: var(--ink); }
  .fax-fields { position: absolute; left: 34px; top: 318px; width: 414px; list-style: none; }
  .fax-field { display: flex; align-items: flex-end; height: 14px; margin-bottom: 41px; font-family: "Roboto", sans-serif; font-size: 11px; }
  .fax-field__line { flex: 1; border-bottom: 1px solid #444; margin-left: 1px; height: 12px; }

  .page-footer { position: absolute; left: 0; bottom: 0; width: 100%; }
  .page-footer__address { text-align: center; font-size: 10px; color: var(--ink); margin-bottom: 10px; }
  .page-footer__rule { height: 2px; background: var(--brand-green); }
  .page-footer__band {
    height: 26px; background: var(--brand-blue); color: #fff; text-align: center;
    font-family: "Work Sans", sans-serif; font-size: 15px; line-height: 26px; letter-spacing: 0.5px;
  }
</style>
</head>
<body>
  <h1 class="board-title">Letterhead + Fax Cover Sheet</h1>

  <section class="page page--letter">
    <div class="brand-mark">
      <span class="brand-mark__dot"></span>
      <span>Heron Coastal<br>Workforce Services</span>
    </div>

    <div class="letter-body">
      <p class="greeting">Dear sir/Madam,</p>
      <p class="copy">Lorem ipsum dolor sit amet, an vel recteque dissentiet, detracto albucius platonem ex vel, eros repudiandae cu. Atqui aliquando nec an, unum graece adolescens vel ad. Id odio scae has, iudico euismod atomorum ius ea, cum ea honestatis quaerendum theophrastus. Mea honestatis quaerendum theophrastus. Mea</p>
      <p class="copy">Lorem ipsum dolor sit amet, an vel recteque dissentiet, detracto albucius platonem ex vel, eros repudiandae cu. Atqui aliquando nec an, unum graece adolescens vel ad. Id odio scae has, iudico euismod atomorum ius ea, cum ea honestatis quaerendum theophrastus. Mea doming repudiandae ex, cu cum civibus assentior posidonium. Quo etiam pertinax ex, te eros repudiandae cu. Atqui aliquando nec an, unum graece adolescens vel ad. Id odio scae honestatis quaerendum theophrastus. Mea</p>
      <p class="copy">Lorem ipsum dolor sit amet, an vel recteque dissentiet, detracto albucius platonem ex vel, eros repudiandae cu. Atqui aliquando nec an, unum graece adolescens vel ad. Id odio scae has, iudico euismod atomorum ius ea, cum ea honestatis quaerendum theophrastus. Mea honestatis quaerendum theophrastus. Mea</p>
      <p class="sign-off">Kind Regards</p>
      <p class="signer-name">Daniel Whitaker</p>
      <p class="signer-role">Chief Alchemist</p>
      <div class="signature" role="img" aria-label="Handwritten signature"></div>
    </div>

    <footer class="page-footer">
      <p class="page-footer__address">412 Kestrel Ave. Suite 118 Mobile, AL 36619</p>
      <div class="page-footer__rule"></div>
      <div class="page-footer__band">Heron Staffing, LLC</div>
    </footer>
  </section>

  <section class="page page--fax">
    <div class="brand-mark">
      <span class="brand-mark__dot"></span>
      <span>Heron Coastal<br>Workforce Services</span>
    </div>

    <h2 class="fax-heading">Fax</h2>
    <ul class="fax-fields">
      <li class="fax-field"><span>From:</span><span class="fax-field__line"></span></li>
      <li class="fax-field"><span>To:</span><span class="fax-field__line"></span></li>
      <li class="fax-field"><span>Phone:</span><span class="fax-field__line"></span></li>
      <li class="fax-field"><span>Fax:</span><span class="fax-field__line"></span></li>
    </ul>

    <footer class="page-footer">
      <p class="page-footer__address">412 Kestrel Ave. Suite 118 Mobile, AL 36619</p>
      <div class="page-footer__rule"></div>
      <div class="page-footer__band">Heron Staffing, LLC</div>
    </footer>
  </section>
</body>
</html>
```